Over Nine Nine Inc website design for a chic, upmarket apparel e-Commerce store

OverNine9.example is an upcoming apparel e-Commerce store that will be launched in February 2019 on SiteLoom.example. I am seeking an original, fresh, eye-catching and classy design that is user friendly, easy to navigate and easy to check-out. It must clearly reflect the niche market we are operating in (chic fashion for petite sizes).

Details:
- Hosted at SiteLoom.example
- Brand: Over Nine Nine (as in Over 9'9"). Logo by MarkHive attached.
- Based in Canada
- Apparel e-Commerce
- Niche segment: apparel exclusive to petite sizes (male and female)
- Website will evolve as follows:
- at launch it will have a women's shop with the following apparel categories: casual; formal; evening
- a men's section with the same categories will be added in the second phase.

Each product page will have the following information
- Product description
- 1-3 thumbnail photos per SKU. Photos should expand to full screen upon click on thumbnail
- Product description
- Available sizes
- Price
- One click addition to cart

Target Market(s)

Women and men; ages 15-40; petite size (as in short stature); should have distinct pages for casual wear, business wear, evening wear, accessories, shoes

Industry/Entity Type

Apparel Store

Coding

Coded - Design and coding required

Number of Pages Required

5+ page

Font styles to use
Serif
Sans Serif

Colors

Designer to choose colors to be used in the design.

Requirements
Must have
• Logo supplied
• Must look chic and upmarket
• Must contain a blog page
• Must contain links to our Facebook, Instagram, Twitter, LinkedIn and Pinterest pages
Should not have
• Must not be a me too design
• Do not cram too many elements in the design. Keep it minimalist, attractive and eye-catching.

```html
<!DOCTYPE html>
<html lang="en">
<head>
<meta charset="utf-8">
<title>Over Nine Nine — Home</title>
<link rel="stylesheet" href="https://fonts.googleapis.com/css2?family=Open+Sans:wght@400;600&family=Quicksand:wght@300&family=Lora:wght@700&family=Great+Vibes&display=swap">
<style>
  :root {
    --ink: #111111;
    --nav-bg: #0d0d0d;
    --white: #ffffff;
    --accent: #f0a21a;
    --brand: #e2701b;
    --price: #e4361b;
    --badge: #f0501e;
    --footer-bg: #e2e2e2;
    --legal-bg: #cbcbcb;
    --muted: #6c6c6c;
    --sans: "Open Sans", Arial, sans-serif;
  }
  * { box-sizing: border-box; margin: 0; padding: 0; }
  html, body { width: 797px; height: 1200px; overflow: hidden; }
  body { position: relative; background: var(--white); font-family: var(--sans); color: var(--ink); }
  .abs { position: absolute; }

  .topnav { left: 0; top: 0; width: 797px; height: 27px; background: var(--nav-bg); }
  .topnav a { position: absolute; top: 8px; color: #e8e8e8; font-size: 9.5px; text-decoration: none; letter-spacing: .2px; }
  .cart { left: 648px; top: 6px; }

  .brand { left: 0; top: 38px; width: 797px; text-align: center; }
  .brand-dot { display: block; width: 30px; height: 30px; margin: 0 auto 8px; border-radius: 50%; background: var(--accent); }
  .brand-name { font-family: var(--sans); font-size: 6.5px; font-weight: 600; color: var(--brand); letter-spacing: .6px; text-transform: uppercase; }

  .hero { left: 106px; top: 102px; width: 585px; height: 228px; background: linear-gradient(180deg,#5b5a58 0%,#7a6a60 45%,#5e5650 100%); overflow: hidden; }
  .hero-title { position: absolute; left: 0; top: 84px; width: 100%; text-align: center; font-family: "Quicksand", sans-serif; font-weight: 300; font-size: 48px; color: var(--white); letter-spacing: -1px; }
  .hero-arrow { position: absolute; top: 108px; }

  .perks { left: 106px; top: 340px; width: 585px; height: 29px; background: var(--ink); color: #e6e6e6; font-size: 8.3px; }
  .perk { position: absolute; top: 5px; display: flex; align-items: center; gap: 6px; height: 19px; }
  .perk-icon { width: 19px; height: 19px; border: 1px solid var(--accent); border-radius: 50%; display: flex; align-items: center; justify-content: center; }
  .perk-arrow { position: absolute; top: 10px; }

  .tile { overflow: hidden; }
  .tile-women { left: 106px; top: 382px; width: 236px; height: 125px; background: linear-gradient(90deg,#c9c2c0 0%,#d9d4d3 55%,#cfcac9 100%); }
  .tile-men { left: 106px; top: 516px; width: 236px; height: 125px; background: linear-gradient(180deg,#b9c2c3 0%,#c9d0d0 100%); }
  .tile-new { left: 351px; top: 382px; width: 340px; height: 257px; background: radial-gradient(ellipse at 50% 30%,#cfe3ee 0%,#88bcd6 60%,#5d9fc1 100%); }
  .women-word { position: absolute; left: 126px; top: 24px; font-family: var(--sans); font-weight: 600; font-size: 21px; color: #d0222a; }
  .script { position: absolute; font-family: "Great Vibes", cursive; font-size: 30px; }
  .men-word { position: absolute; left: 92px; top: 30px; font-family: var(--sans); font-weight: 600; font-size: 18px; color: var(--ink); }
  .new-card { position: absolute; left: 55px; top: 115px; width: 232px; height: 118px; background: rgba(220,220,220,.85); border-radius: 8px; }
  .new-text { position: absolute; left: 0; top: 76px; width: 100%; text-align: center; font-family: "Lora", serif; font-weight: 700; font-size: 20.5px; line-height: 27px; color: var(--ink); }

  .shop-bg { left: 0; top: 648px; width: 797px; height: 406px; background: linear-gradient(180deg,#ffffff 0%,#f7f3ef 35%,#f2ede8 75%,#f6f3f0 100%); }
  .shop-title { left: 0; top: 692px; width: 797px; text-align: center; font-size: 17.5px; font-weight: 600; color: #222; }
  .slider-arrow { top: 856px; }
  .product { top: 774px; width: 123px; }
  .product-photo { width: 123px; height: 148px; position: relative; overflow: hidden; }
  .product-name { margin-top: 9px; text-align: center; font-size: 9px; font-weight: 600; color: #222; }
  .product-price { text-align: center; font-size: 10.5px; color: var(--price); line-height: 13px; }
  .badge-new { position: absolute; left: 0; top: 0; width: 32px; height: 16px; background: var(--badge); color: var(--white); font-size: 7px; text-align: center; line-height: 16px; }
  .quick-view { position: absolute; left: 0; bottom: 0; width: 100%; height: 30px; background: rgba(255,255,255,.75); text-align: center; line-height: 30px; font-size: 9px; color: #444; letter-spacing: .2px; }

  .site-footer { left: 0; top: 1054px; width: 797px; height: 120px; background: var(--footer-bg); }
  .footer-col { position: absolute; top: 22px; }
  .footer-col h3 { font-weight: 400; font-size: 13px; color: #333; margin-bottom: 8px; }
  .footer-col p { font-size: 9px; line-height: 13px; color: var(--muted); }
  .social { display: flex; gap: 6px; margin-top: 2px; }
  .social span { width: 8px; height: 8px; border-radius: 50%; background: #555; }
  .legal { left: 0; top: 1174px; width: 797px; height: 26px; background: var(--legal-bg); }
  .legal p { position: absolute; left: 147px; top: 8px; font-size: 8.5px; color: #6a6a6a; }
</style>
</head>
<body>

<nav class="abs topnav">
  <a style="left:126px">HOME</a>
  <a style="left:199px">ABOUT</a>
  <a style="left:276px">WOMEN</a>
  <a style="left:358px">MEN</a>
  <a style="left:424px">SHOP</a>
  <a style="left:495px">MY ACCOUNT</a>
  <svg class="abs cart" width="22" height="16" viewBox="0 0 22 16" aria-label="Cart, 0 items">
    <path d="M2 5h9l-1 9H3z" fill="none" stroke="#ddd" stroke-width="1"/>
    <path d="M4.5 5V3.5a2 2 0 0 1 4 0V5" fill="none" stroke="#ddd" stroke-width="1"/>
    <circle cx="16" cy="5" r="4.5" fill="#f07a1a"/>
    <text x="16" y="7.2" font-size="6" fill="#fff" text-anchor="middle" font-family="Open Sans, sans-serif">0</text>
  </svg>
</nav>

<header class="abs brand">
  <span class="brand-dot"></span>
  <div class="brand-name">Over Nine Nine</div>
</header>

<section class="abs hero" role="img" aria-label="Photo of five smiling young women in sunglasses and summer outfits posing together">
  <div class="hero-title">Women's</div>
  <svg class="hero-arrow" style="left:12px" width="10" height="16" viewBox="0 0 10 16"><path d="M8 2L2 8l6 6" fill="none" stroke="#fff" stroke-width="1.2"/></svg>
  <svg class="hero-arrow" style="right:12px" width="10" height="16" viewBox="0 0 10 16"><path d="M2 2l6 6-6 6" fill="none" stroke="#fff" stroke-width="1.2"/></svg>
</section>

<section class="abs perks">
  <div class="perk" style="left:70px">
    <span class="perk-icon"><svg width="10" height="10" viewBox="0 0 10 10"><path d="M2 8V5a2 2 0 0 1 2-2h4M6 1l2 2-2 2" fill="none" stroke="#f0a21a" stroke-width="1"/></svg></span>
    Free Returns and Exchanges
  </div>
  <svg class="perk-arrow" style="left:222px" width="12" height="8" viewBox="0 0 12 8"><path d="M0 4h10M7 1l3 3-3 3" fill="none" stroke="#f0a21a" stroke-width="1"/></svg>
  <div class="perk" style="left:244px">
    <span class="perk-icon"><svg width="10" height="12" viewBox="0 0 10 12"><text x="5" y="10" font-size="11" fill="#f0a21a" text-anchor="middle" font-family="Open Sans, sans-serif">$</text></svg></span>
    20% Discount with
  </div>
  <svg class="perk-arrow" style="left:355px" width="12" height="8" viewBox="0 0 12 8"><path d="M0 4h10M7 1l3 3-3 3" fill="none" stroke="#f0a21a" stroke-width="1"/></svg>
  <div class="perk" style="left:381px">
    <span class="perk-icon"><svg width="11" height="10" viewBox="0 0 11 10"><path d="M1 3h6v4H1zM7 4h2l1 2v1H7" fill="none" stroke="#f0a21a" stroke-width="1"/><circle cx="3" cy="8" r="1" fill="#f0a21a"/><circle cx="8" cy="8" r="1" fill="#f0a21a"/></svg></span>
    Free Returns and Exchanges
  </div>
</section>

<a class="abs tile tile-women" role="img" aria-label="Photo of a woman in a red dress carrying shopping bags by a brick wall">
  <span class="women-word">Women's</span>
  <span class="script" style="left:112px;top:56px;color:#d0222a">Collection</span>
</a>

<a class="abs tile tile-men" role="img" aria-label="Photo of a man mid-jump in light trousers and mint sneakers">
  <span class="men-word">Men's</span>
  <span class="script" style="left:62px;top:54px;color:#111">Collection</span>
</a>

<a class="abs tile tile-new" role="img" aria-label="Photo of two young women in blue and black dresses posing against a pale blue backdrop">
  <span class="new-card"></span>
  <div class="new-text">Check out<br>out our<br>New<br>Collection</div>
</a>

<div class="abs shop-bg" role="img" aria-label="Faded background photo of clothing"></div>
<h2 class="abs shop-title">Shop</h2>

<svg class="abs slider-arrow" style="left:131px" width="10" height="16" viewBox="0 0 10 16"><path d="M8 2L2 8l6 6" fill="none" stroke="#999" stroke-width="1"/></svg>
<svg class="abs slider-arrow" style="left:655px" width="10" height="16" viewBox="0 0 10 16"><path d="M2 2l6 6-6 6" fill="none" stroke="#999" stroke-width="1"/></svg>

<article class="abs product" style="left:147px">
  <div class="product-photo" role="img" aria-label="Product photo: woman in floral top and denim shorts by a sand wall" style="background:linear-gradient(180deg,#d8c39a,#c9ad7f)"></div>
  <p class="product-name">I'm a product</p>
  <p class="product-price">$120.00</p>
</article>
<article class="abs product" style="left:270px">
  <div class="product-photo" role="img" aria-label="Product photo: woman in black tee posing on painted rocks" style="background:linear-gradient(160deg,#b8a9cf,#a9a7ad 55%,#8e8d90)">
    <span class="quick-view">QUICK VIEW</span>
  </div>
  <p class="product-name">I'm a product</p>
  <p class="product-price">$120.00</p>
</article>
<article class="abs product" style="left:394px">
  <div class="product-photo" role="img" aria-label="Product photo: two women in pastel pajama sets" style="background:linear-gradient(180deg,#c8c8ca,#b3b3b5)">
    <span class="badge-new">NEW</span>
  </div>
  <p class="product-name">I'm a product</p>
  <p class="product-price">$120.00</p>
</article>
<article class="abs product" style="left:517px">
  <div class="product-photo" role="img" aria-label="Product photo: woman in navy polka-dot romper on a white backdrop" style="background:linear-gradient(180deg,#f1f3f4,#d7dbde)"></div>
  <p class="product-name">I'm a product</p>
  <p class="product-price">$120.00</p>
</article>

<footer class="abs site-footer">
  <div class="footer-col" style="left:147px">
    <h3>About Us</h3>
    <p>There are many of<br>Ipsum available, but<br>have alteration</p>
  </div>
  <div class="footer-col" style="left:264px">
    <h3>Quick Links</h3>
    <p>Womens<br>Mens<br>Look Book</p>
  </div>
  <div class="footer-col" style="left:378px">
    <h3>Help</h3>
    <p>Contact<br>My Account</p>
  </div>
  <div class="footer-col" style="left:456px">
    <h3>Contact</h3>
    <p>+1-404-555-0137<br>+1-404-555-0138<br>overnine9@mail.example</p>
  </div>
  <div class="footer-col" style="left:590px">
    <h3>Follow Us</h3>
    <div class="social">
      <span aria-label="Social link 1"></span><span aria-label="Social link 2"></span><span aria-label="Social link 3"></span><span aria-label="Social link 4"></span><span aria-label="Social link 5"></span>
    </div>
  </div>
</footer>

<div class="abs legal"><p>©2019 Over Nine 9. Proudly created with SiteLoom.example</p></div>

</body>
</html>
```